Flyer for a marketing

We are a holistic mental health facility in need of a flyer to help promote our services and encourage more people to seek care. See the attachment to tell you more. We prefer warm green colors or rich blue. Thank you.

```html
<!DOCTYPE html>
<html lang="en">
<head>
<meta charset="utf-8">
<title>Evergreen Mind Health and Wellness – Flyer</title>
<link rel="stylesheet" href="https://fonts.googleapis.com/css2?family=Merriweather:wght@700;900&family=Poppins:wght@400;500;600&display=swap">
<style>
  :root {
    --green-dark: #2c5a22;
    --green-mid: #4c8a32;
    --green-light: #5f9b3c;
    --green-band: #2f5a25;
    --orange: #e8971f;
    --orange-deep: #d9821a;
    --ink: #1f261d;
    --slate: #4a4640;
    --paper: #e4e6e8;
    --white: #ffffff;
  }
  * { margin: 0; padding: 0; box-sizing: border-box; }
  html, body { width: 1200px; height: 2824px; overflow: hidden; }
  body { background: var(--paper); position: relative; font-family: "Poppins", sans-serif; }

  .flyer {
    position: absolute; left: 40px; top: 621px;
    width: 935px; height: 1320px;
    transform: scale(1.1979); transform-origin: top left;
    overflow: hidden;
    box-shadow: 0 10px 30px rgba(0,0,0,.25);
  }
  .flyer__backdrop { position: absolute; inset: 0; }
  .flyer__top-band {
    position: absolute; left: 0; top: 0; width: 100%; height: 22px;
    background: linear-gradient(180deg, #24481c, #3f6b2e 70%, rgba(90,110,70,0));
  }

  .brand { position: absolute; left: 30px; top: 92px; display: flex; align-items: center; gap: 22px; }
  .brand__dot { width: 96px; height: 96px; border-radius: 50%; background: var(--white); flex: none; }
  .brand__name {
    font-family: "Merriweather", serif; font-weight: 700; color: var(--white);
    font-size: 21px; line-height: 26px;
  }

  .slogan { position: absolute; right: 22px; top: 68px; width: 330px; height: 200px; font-family: "Merriweather", serif; font-weight: 900; }
  .slogan span { position: absolute; white-space: nowrap; line-height: 1; }
  .slogan__the { color: var(--slate); font-size: 46px; left: 118px; top: 10px; }
  .slogan__care { color: var(--green-dark); font-size: 78px; left: 0; top: 46px; }
  .slogan__you { color: var(--slate); font-size: 46px; left: 220px; top: 74px; }
  .slogan__deserve { color: var(--orange-deep); font-size: 64px; left: 56px; top: 128px; }

  .photo-cluster { position: absolute; left: 0; top: 40px; }

  .headline {
    position: absolute; left: 0; top: 628px; width: 935px; text-align: center;
    font-weight: 600; color: var(--green-dark); font-size: 39px; line-height: 45px;
  }
  .headline__mid { color: var(--green-mid); }
  .headline__accent { color: var(--orange); }
  .tagline {
    position: absolute; left: 52px; top: 770px; width: 860px;
    font-weight: 600; color: var(--green-dark); font-size: 27.5px; white-space: nowrap;
  }

  .intro { position: absolute; left: 52px; top: 845px; width: 560px; }
  .intro__lead { color: var(--green-light); font-weight: 600; font-size: 21px; margin-bottom: 4px; }
  .intro__text { color: var(--ink); font-size: 17px; line-height: 21px; }

  .reasons { position: absolute; left: 52px; top: 955px; width: 560px; color: var(--ink); }
  .reasons__title { color: var(--green-dark); font-weight: 600; font-size: 18.5px; margin-bottom: 16px; }
  .reasons__list { list-style: none; font-size: 17px; line-height: 21px; }
  .reasons__list li { margin-bottom: 17px; }

  .side-image { position: absolute; border-radius: 10px; box-shadow: 0 2px 6px rgba(0,0,0,.2); border: 2px solid #f2f2f2; }
  .side-image--session { left: 633px; top: 843px; width: 254px; height: 170px; background: linear-gradient(135deg, #d9d3c6, #b8b1a2 40%, #7b8592 60%, #e9e6df); }
  .side-image--minds { left: 640px; top: 1045px; width: 247px; height: 183px; background: radial-gradient(circle at 28% 35%, #d88b6a 0 18%, transparent 34%), radial-gradient(circle at 75% 35%, #9a6fb8 0 16%, transparent 32%), #f1f1f2; }

  .footer {
    position: absolute; left: 0; top: 1236px; width: 100%; height: 84px;
    border-top: 5px solid var(--orange);
    background: linear-gradient(180deg, #2f5d26, #24491d);
    font-size: 15px; line-height: 22px;
  }
  .footer__col { position: absolute; top: 17px; }
  .footer__col--address { left: 16px; color: var(--white); }
  .footer__col--address strong { color: var(--orange); font-weight: 600; }
  .footer__col--phones { left: 443px; color: var(--orange); font-weight: 600; font-size: 16px; }
  .footer__label { font-size: 13px; margin-right: 4px; }
  .footer__col--online { left: 628px; color: #8fcf5b; font-weight: 500; font-size: 16px; }
</style>
</head>
<body>
  <main class="flyer">
    <svg class="flyer__backdrop" width="935" height="1320" viewBox="0 0 935 1320" role="img" aria-label="Sunset sky over a misty forest fading to white">
      <defs>
        <linearGradient id="sky" x1="0" y1="0" x2="0" y2="1">
          <stop offset="0" stop-color="#6f6862"/>
          <stop offset="0.06" stop-color="#b48b66"/>
          <stop offset="0.2" stop-color="#e3b784"/>
          <stop offset="0.34" stop-color="#d9c9b2"/>
          <stop offset="0.5" stop-color="#ebebea"/>
          <stop offset="0.75" stop-color="#dfe0df"/>
          <stop offset="1" stop-color="#f3f3f3"/>
        </linearGradient>
      </defs>
      <rect width="935" height="1320" fill="url(#sky)"/>
    </svg>
    <div class="flyer__top-band"></div>

    <div class="brand">
      <span class="brand__dot"></span>
      <span class="brand__name">Evergreen<br>Mind<br>Health<br>and<br>Wellness</span>
    </div>

    <div class="slogan" aria-label="The Care You Deserve">
      <span class="slogan__the">The</span>
      <span class="slogan__care">Care</span>
      <span class="slogan__you">You</span>
      <span class="slogan__deserve">Deserve</span>
    </div>

    <svg class="photo-cluster" width="935" height="620" viewBox="0 40 935 620">
      <defs>
        <linearGradient id="photoFamily" x1="0" y1="0" x2="1" y2="1">
          <stop offset="0" stop-color="#7a6a52"/><stop offset="0.45" stop-color="#6f8aa0"/><stop offset="1" stop-color="#d8c7b0"/>
        </linearGradient>
        <linearGradient id="photoPortrait" x1="0" y1="0" x2="1" y2="1">
          <stop offset="0" stop-color="#3a2a22"/><stop offset="0.5" stop-color="#a77456"/><stop offset="1" stop-color="#cfd2cf"/>
        </linearGradient>
        <linearGradient id="photoPark" x1="0" y1="0" x2="0" y2="1">
          <stop offset="0" stop-color="#3f5d33"/><stop offset="0.5" stop-color="#6f9a3e"/><stop offset="1" stop-color="#9bbf3c"/>
        </linearGradient>
      </defs>
      <g role="img" aria-label="Photo of a grandmother pouring a warm drink for a girl outdoors">
        <rect x="-135" y="-135" width="270" height="270" rx="40" transform="translate(462 275) rotate(45) scale(1 1.06)" fill="url(#photoFamily)" stroke="#f7efe6" stroke-width="4"/>
      </g>
      <g role="img" aria-label="Photo of a smiling young woman with curly hair">
        <rect x="-145" y="-145" width="290" height="290" rx="42" transform="translate(218 510) rotate(45)" fill="url(#photoPortrait)" stroke="#f4f1ec" stroke-width="4"/>
      </g>
      <g role="img" aria-label="Photo of a family playing together in a green park">
        <rect x="-145" y="-145" width="290" height="290" rx="42" transform="translate(712 510) rotate(45)" fill="url(#photoPark)" stroke="#f4f1ec" stroke-width="4"/>
      </g>
    </svg>

    <h1 class="headline">EVERGREEN<br><span class="headline__mid">MIND HEALTH</span><br>AND <span class="headline__accent">WELLNESS</span>,</h1>
    <p class="tagline">where deserving patients meet compassionate providers.</p>

    <section class="intro">
      <p class="intro__lead">We are accepting new patients, no waiting list.</p>
      <p class="intro__text">Your mental health matters, so make it a priority and call us<br>today for an appointment.</p>
    </section>

    <section class="reasons">
      <h2 class="reasons__title">Why choose us?</h2>
      <ul class="reasons__list">
        <li>We are an integrative holistic psychiatric center.</li>
        <li>Our mission is to provide compassionate quality care.</li>
        <li>We provide psychiatric services including medication<br>management and psychotherapy.</li>
        <li>We listen, care, and empower you to live better.</li>
        <li>We accept major insurances.</li>
      </ul>
    </section>

    <div class="side-image side-image--session" role="img" aria-label="Photo of a distressed woman talking with a therapist"></div>
    <div class="side-image side-image--minds" role="img" aria-label="Illustration of two head outlines filled with colourful puzzle blocks"></div>

    <footer class="footer">
      <div class="footer__col footer__col--address">
        <strong>Evergreen Mind Health and Wellness, APNC</strong><br>
        1850 Maple Ridge Road, Suite 300 Fairview, CA 90210
      </div>
      <div class="footer__col footer__col--phones">
        <span class="footer__label">Ph</span> (555) 214-7730<br>
        <span class="footer__label">Fax</span> (555) 214-7731
      </div>
      <div class="footer__col footer__col--online">
        info@evergreenmindhealth.com<br>
        evergreenmindhealth.com
      </div>
    </footer>
  </main>
</body>
</html>
```